Marlow Estates Business Card and Email Signature Design

I am a Homevant and need a business card design with my head shot picture and logo and contact information that can be prepared to be used on my email signature as well. I would like my head shot image background to match the background of the business card. So in other words the background of my head shot should be transparent. I would like the Homevant Logo on there and also PRX and Fair Dwelling Logo. My email address is: ted@marlowestates.example, Phone Number is: 555-014-7391, website: www.marlowestates.example Address: 48207 Quillfern Court Fernvale, ZZ 99014
I also need just the head shot photo with white background in a JPEG file as well so I can upload that picture to my Jobtrellis and Nestavo profiles.

```html
<!DOCTYPE html>
<html lang="en">
<head>
<meta charset="utf-8">
<title>Marlow Estates Business Cards</title>
<link href="https://fonts.googleapis.com/css2?family=Exo+2:wght@600;700&family=Lato:wght@400;700&display=swap" rel="stylesheet">
<style>
  :root {
    --brand-blue: #0a6aa1;
    --brand-blue-deep: #07507d;
    --brand-blue-light: #1a86c2;
    --stripe-grey: #5d5f63;
    --paper: #f7f8f9;
    --ink: #3c3f44;
    --backdrop: #e9e6e1;
    --white: #ffffff;
  }
  * { box-sizing: border-box; margin: 0; padding: 0; }
  html, body { width: 1200px; height: 780px; overflow: hidden; }
  body {
    background: var(--backdrop);
    position: relative;
    font-family: "Lato", Arial, sans-serif;
  }
  .card {
    position: absolute;
    top: 235px;
    width: 540px;
    height: 309px;
    border-radius: 4px;
    overflow: hidden;
    box-shadow: 0 6px 18px rgba(0,0,0,0.18);
  }
  .card--front { left: 40px; background: var(--brand-blue); }
  .card--back {
    left: 620px;
    background: radial-gradient(ellipse at 40% 45%, var(--brand-blue-light) 0%, var(--brand-blue) 55%, var(--brand-blue-deep) 100%);
  }
  .front-shapes { position: absolute; inset: 0; }
  .headshot {
    position: absolute;
    right: 0;
    top: 8px;
    width: 190px;
    height: 142px;
    background: linear-gradient(180deg, #eceff2 0%, #cdd3da 45%, #1c2638 100%);
  }
  .owner {
    position: absolute;
    left: 22px;
    bottom: 26px;
    color: var(--white);
  }
  .owner__name {
    font-family: "Exo 2", Arial, sans-serif;
    font-weight: 700;
    font-size: 17px;
    letter-spacing: 0.5px;
    text-transform: uppercase;
  }
  .owner__title { font-size: 13px; line-height: 1; }
  .front-brand {
    position: absolute;
    left: 196px;
    top: 160px;
  }
  .front-brand__name {
    font-family: "Exo 2", Arial, sans-serif;
    font-weight: 700;
    font-size: 27px;
    color: var(--brand-blue);
    text-transform: uppercase;
    line-height: 1;
  }
  .front-brand__tagline {
    font-size: 9.5px;
    font-weight: 700;
    letter-spacing: 2.6px;
    color: var(--ink);
    text-transform: uppercase;
    margin-top: 3px;
  }
  .contact-list {
    position: absolute;
    left: 196px;
    top: 212px;
    list-style: none;
  }
  .contact-list li {
    display: flex;
    align-items: center;
    gap: 7px;
    font-size: 12.5px;
    color: var(--ink);
    height: 19px;
    white-space: nowrap;
  }
  .contact-icon { width: 13px; height: 13px; flex: none; }
  .back-brand {
    position: absolute;
    inset: 0;
    display: flex;
    align-items: center;
    justify-content: center;
    gap: 22px;
    color: var(--white);
  }
  .back-brand__mark {
    width: 82px;
    height: 82px;
    border-radius: 50%;
    background: var(--white);
  }
  .back-brand__name {
    font-family: "Exo 2", Arial, sans-serif;
    font-weight: 700;
    font-size: 32px;
    text-transform: uppercase;
    line-height: 1;
  }
  .back-brand__tagline {
    font-size: 11px;
    font-weight: 700;
    letter-spacing: 3.4px;
    text-transform: uppercase;
    margin-top: 5px;
  }
</style>
</head>
<body>

<section class="card card--front" aria-label="Business card front">
  <svg class="front-shapes" viewBox="0 0 540 309" aria-hidden="true">
    <polygon points="150,0 540,0 540,309 150,309 110,154" fill="#5d5f63"/>
    <polygon points="172,0 540,0 540,309 172,309 132,154" fill="#f7f8f9"/>
    <polygon points="150,0 540,0 540,8 146,8" fill="#0a6aa1"/>
  </svg>
  <div class="headshot" role="img" aria-label="Headshot of the owner on a transparent background"></div>

  <div class="owner">
    <p class="owner__name">Ted Harrow</p>
    <p class="owner__title">owner</p>
  </div>

  <div class="front-brand">
    <p class="front-brand__name">Marlow Estates</p>
    <p class="front-brand__tagline">Real Estate Services</p>
  </div>

  <ul class="contact-list">
    <li>
      <svg class="contact-icon" viewBox="0 0 14 14" aria-hidden="true"><circle cx="7" cy="7" r="6.3" fill="none" stroke="#0a6aa1" stroke-width="1"/><rect x="5" y="3.5" width="4" height="7" rx="0.8" fill="#0a6aa1"/></svg>
      555-014-7391
    </li>
    <li>
      <svg class="contact-icon" viewBox="0 0 14 14" aria-hidden="true"><circle cx="7" cy="7" r="6.3" fill="none" stroke="#0a6aa1" stroke-width="1"/><rect x="3.5" y="4.5" width="7" height="5" fill="#0a6aa1"/><polyline points="3.5,4.5 7,7.5 10.5,4.5" fill="none" stroke="#fff" stroke-width="0.8"/></svg>
      ted@marlowestates.example
    </li>
    <li>
      <svg class="contact-icon" viewBox="0 0 14 14" aria-hidden="true"><circle cx="7" cy="7" r="6.3" fill="none" stroke="#0a6aa1" stroke-width="1"/><circle cx="7" cy="7" r="3.6" fill="none" stroke="#0a6aa1" stroke-width="0.9"/><line x1="3.4" y1="7" x2="10.6" y2="7" stroke="#0a6aa1" stroke-width="0.8"/><ellipse cx="7" cy="7" rx="1.5" ry="3.6" fill="none" stroke="#0a6aa1" stroke-width="0.8"/></svg>
      www.marlowestates.example
    </li>
    <li>
      <svg class="contact-icon" viewBox="0 0 14 14" aria-hidden="true"><circle cx="7" cy="7" r="6.3" fill="none" stroke="#0a6aa1" stroke-width="1"/><path d="M7 11 C5 8.5 4.4 7.4 4.4 6 A2.6 2.6 0 0 1 9.6 6 C9.6 7.4 9 8.5 7 11 Z" fill="#0a6aa1"/><circle cx="7" cy="6" r="0.9" fill="#fff"/></svg>
      48207 Quillfern Court Fernvale, ZZ 99014
    </li>
  </ul>
</section>

<section class="card card--back" aria-label="Business card back">
  <div class="back-brand">
    <div>
      <p class="back-brand__name">Marlow Estates</p>
      <p class="back-brand__tagline">Real Estate Services</p>
    </div>
    <span class="back-brand__mark" aria-hidden="true"></span>
  </div>
</section>

</body>
</html>
```